Business Card Design

Im looking for a business card that will market/promote myself as in independent/freelancer in the beauty industry. Im looking for something very modern, and clean looking. no specific colors just something that doesnt look cheesy, would like a very professional look

Industry/Entity Type

Business

Contact Information for Business Card

Corinne Balstrade, Hairstylist(Cut, color, blowdry, style, extensions, straightening treatments), makeup artist, red carpet, in-salon, editorial, tv, film, contact is 5307419863 cbglam@mailbrook.net, LA based

```html
<!DOCTYPE html>
<html lang="en">
<head>
<meta charset="utf-8">
<title>Corinne Balstrade – Business Card</title>
<link href="https://fonts.googleapis.com/css2?family=Questrial&display=swap" rel="stylesheet">
<style>
  :root {
    --page-bg: #ffffff;
    --label-grey: #8a8a8a;
    --pink-deep: #e94c9a;
    --pink-light: #f48dba;
    --pink-accent: #ea5a9f;
    --ink-dark: #3e3e3e;
    --ink-body: #333333;
    --card-border: #c9c9c9;
  }
  * { margin: 0; padding: 0; box-sizing: border-box; }
  html, body {
    width: 867px; height: 1200px; overflow: hidden;
    background: var(--page-bg);
    font-family: "Questrial", "Century Gothic", sans-serif;
  }
  .sheet { position: relative; width: 867px; height: 1200px; }
  .side-label {
    position: absolute; left: 0; width: 100%;
    text-align: center; font-size: 38px; color: var(--label-grey);
  }
  .side-label--front { top: 78px; }
  .side-label--back { top: 632px; }
  .card { position: absolute; left: 77px; width: 713px; height: 418px; }
  .card--front {
    top: 161px;
    background: linear-gradient(90deg, var(--pink-deep), var(--pink-light));
  }
  .card--back {
    top: 704px; background: #fff; border: 2px solid var(--card-border);
  }
  .wordmark { position: absolute; line-height: 1.02; }
  .wordmark--front {
    left: 288px; top: 262px; font-size: 58px; color: var(--ink-dark);
  }
  .wordmark--back {
    left: 41px; top: 196px; font-size: 42px; color: var(--pink-accent);
  }
  .details { position: absolute; left: 350px; top: 90px; color: var(--ink-body); }
  .details__title { font-size: 19px; letter-spacing: 0.5px; margin-bottom: 20px; }
  .details__services { font-size: 16.5px; line-height: 28px; margin-bottom: 24px; }
  .contact { display: flex; align-items: center; gap: 8px; font-size: 19px; margin-bottom: 10px; }
  .contact__icon { width: 26px; height: 26px; flex: none; }
</style>
</head>
<body>
<div class="sheet">
  <div class="side-label side-label--front">Front</div>
  <section class="card card--front">
    <div class="wordmark wordmark--front">Corinne<br>Balstrade</div>
  </section>

  <div class="side-label side-label--back">Back</div>
  <section class="card card--back">
    <div class="wordmark wordmark--back">Corinne<br>Balstrade</div>
    <div class="details">
      <p class="details__title">LA BASED HAIRSTYLIST</p>
      <p class="details__services">
        Cut, Color, Blow-dry, Style,<br>
        Extensions, Straightening Treatments<br>
        Makeup Artist - Red Carpet, In-salon<br>
        Editorial, Tv, Film
      </p>
      <div class="contact">
        <svg class="contact__icon" viewBox="0 0 26 26" aria-hidden="true">
          <circle cx="13" cy="13" r="13" fill="var(--pink-accent)"/>
          <path d="M9 7.5c.6-.5 1.4-.4 1.8.2l1.2 1.8c.3.5.2 1.1-.2 1.5l-.8.7c.7 1.5 1.8 2.6 3.3 3.3l.7-.8c.4-.4 1-.5 1.5-.2l1.8 1.2c.6.4.7 1.2.2 1.8l-.9 1c-.6.6-1.5.8-2.3.5C11.7 17.3 8.7 14.3 7.5 10.7c-.3-.8-.1-1.7.5-2.3z" fill="#fff"/>
        </svg>
        <span>5307419863</span>
      </div>
      <div class="contact">
        <svg class="contact__icon" viewBox="0 0 26 26" aria-hidden="true">
          <circle cx="13" cy="13" r="13" fill="var(--pink-accent)"/>
          <rect x="6.5" y="8.5" width="13" height="9" rx="1" fill="#fff"/>
          <path d="M7 9.2l6 4.6 6-4.6" fill="none" stroke="var(--pink-accent)" stroke-width="1.2"/>
        </svg>
        <span>cbglam@mailbrook.net</span>
      </div>
    </div>
  </section>
</div>
</body>
</html>
```